Lanternfield Drinks business cards

We need a business card design for our new logo. The company is modern, progressive, professional, yet approachable. The key products are ready to drink bottles and cans of coffee based beverages.
These cards will be a critical part of the first impression made by our sales organization, business development team, and all external facing personnel.
Card can be a vertical or horizontal orientation.

Target Market(s)

Customers, suppliers, business partners

Industry/Entity Type

Business

Contact Information for Business Card

Business cards should feature Company Name and Logo.

Font styles to use
Serif

Colors

Designer to choose colors to be used in the design.

Requirements
Must have
• Strong readability of Name, phone #, mobile number and email address.
• Job title, website url, Street Address, and other details can be secondary level readability.
Nice to have
• High impact, simplistic quality design.
• Ok to utilize the 'H in the box' separate from the company name

```html
<!DOCTYPE html>
<html lang="en">
<head>
<meta charset="utf-8">
<title>Lanternfield Drinks – Business Cards</title>
<link rel="stylesheet" href="https://fonts.googleapis.com/css2?family=Merriweather:wght@300;400;700&display=swap">
<style>
  :root {
    --stage: #1b1b1b;
    --paper: #ffffff;
    --paper-shade: #f1f1f1;
    --orange: #ee6a2c;
    --orange-deep: #e4582a;
    --amber: #f5a531;
    --gold: #e3a52c;
    --ink: #3a3a3a;
    --mist: #d9d9d9;
  }
  * { box-sizing: border-box; margin: 0; padding: 0; }
  html, body { width: 1200px; height: 864px; overflow: hidden; }
  body {
    background: var(--stage);
    font-family: "Merriweather", serif;
    position: relative;
  }
  .card {
    position: absolute;
    top: 282px;
    width: 525px;
    height: 300px;
    overflow: hidden;
  }
  /* Front */
  .card-front { left: 50px; background: linear-gradient(180deg, var(--paper) 55%, var(--paper-shade)); }
  .brand {
    position: absolute; left: 34px; top: 30px;
    display: flex; align-items: center; gap: 10px;
  }
  .brand-square { width: 26px; height: 26px; background: var(--orange); }
  .brand-name {
    font-size: 20px; font-weight: 700; color: var(--orange); letter-spacing: .3px;
  }
  .accent-bar {
    position: absolute; left: 0; top: 88px; width: 6px; height: 28px; background: var(--amber);
  }
  .person { position: absolute; left: 34px; top: 88px; }
  .person-name {
    font-size: 15px; font-weight: 700; color: var(--orange); text-transform: uppercase; letter-spacing: .4px;
  }
  .person-title { font-size: 11px; color: var(--ink); margin-top: 2px; }
  .contacts { position: absolute; left: 34px; top: 148px; list-style: none; }
  .contacts li {
    display: flex; align-items: center; gap: 12px;
    font-size: 11.5px; font-weight: 300; color: var(--ink); height: 22px;
  }
  .contacts svg { width: 14px; height: 14px; flex: none; }
  .watermark-square {
    position: absolute; left: 350px; top: 100px; width: 140px; height: 140px;
    border: 2px solid #ececec;
  }
  .address-band {
    position: absolute; left: 0; bottom: 18px; width: 100%; height: 40px;
    background: linear-gradient(90deg, var(--orange-deep), var(--amber));
    display: flex; align-items: center; padding-left: 34px;
  }
  .address { font-size: 11px; font-weight: 300; color: var(--paper); }
  .gold-strip {
    position: absolute; left: 0; bottom: 0; width: 100%; height: 18px; background: var(--gold);
  }
  /* Back */
  .card-back {
    left: 625px;
    background: linear-gradient(120deg, var(--amber) 0%, #f48a36 45%, var(--orange-deep) 100%);
  }
  .back-band {
    position: absolute; left: 0; bottom: 0; width: 100%; height: 52px; background: var(--mist);
  }
  .faint-row { position: absolute; left: 22px; top: 70px; display: flex; gap: 16px; }
  .faint-row span {
    width: 58px; height: 58px; border: 2px solid rgba(255,255,255,.22);
  }
  .back-mark {
    position: absolute; right: 40px; top: 104px; width: 128px; height: 128px;
    border: 5px solid var(--paper);
  }
  .back-name {
    position: absolute; left: 26px; top: 168px;
    font-size: 22px; font-weight: 700; color: var(--paper);
  }
</style>
</head>
<body>
  <section class="card card-front" aria-label="Business card front">
    <div class="brand">
      <div class="brand-square"></div>
      <div class="brand-name">Lanternfield Drinks</div>
    </div>
    <div class="accent-bar"></div>
    <div class="person">
      <div class="person-name">Daniel Ostrow</div>
      <div class="person-title">Managing Director</div>
    </div>
    <ul class="contacts">
      <li>
        <svg viewBox="0 0 14 14"><rect x=".5" y=".5" width="13" height="13" fill="none" stroke="#f5a531"/><path d="M4 3.5l1.5 0 .7 2-1 .8a5 5 0 0 0 2.5 2.5l.8-1 2 .7 0 1.5c-4 .3-6.8-2.5-6.5-6.5z" fill="#f5a531"/></svg>
        555.014.2270
      </li>
      <li>
        <svg viewBox="0 0 14 14"><rect x=".5" y=".5" width="13" height="13" fill="none" stroke="#f5a531"/><rect x="4.5" y="2.5" width="5" height="9" rx="1" fill="none" stroke="#f5a531"/><circle cx="7" cy="10" r=".6" fill="#f5a531"/></svg>
        555.018.3391
      </li>
      <li>
        <svg viewBox="0 0 14 14"><rect x=".5" y=".5" width="13" height="13" fill="none" stroke="#f5a531"/><rect x="3" y="4" width="8" height="6" fill="none" stroke="#f5a531"/><path d="M3 4l4 3 4-3" fill="none" stroke="#f5a531"/></svg>
        dan@lanternfielddrinks.com
      </li>
      <li>
        <svg viewBox="0 0 14 14"><rect x=".5" y=".5" width="13" height="13" fill="none" stroke="#f5a531"/><circle cx="7" cy="7" r="4" fill="none" stroke="#f5a531"/><path d="M3 7h8M7 3c-2 2.5-2 5.5 0 8M7 3c2 2.5 2 5.5 0 8" fill="none" stroke="#f5a531" stroke-width=".8"/></svg>
        www.lanternfielddrinks.com
      </li>
    </ul>
    <div class="watermark-square"></div>
    <div class="address-band"><span class="address">48 Meridian Ave, Halden, NY 11590</span></div>
    <div class="gold-strip"></div>
  </section>

  <section class="card card-back" aria-label="Business card back">
    <div class="back-band"></div>
    <div class="faint-row"><span></span><span></span><span></span><span></span></div>
    <div class="back-name">Lanternfield Drinks</div>
    <div class="back-mark"></div>
  </section>
</body>
</html>
```